Mosvane Design

Looking for Mosvane banner and square design:
Mosvane Banner
W:1600 px H:400 px
Square
120x120

Logo attached.

Description: Data-Driven stock market portfolio management using quantitative analysis.

```html
<!DOCTYPE html>
<html lang="en">
<head>
<meta charset="utf-8">
<title>Mosvane Banner and Square Set</title>
<link rel="stylesheet" href="https://fonts.googleapis.com/css2?family=Poppins:wght@400;600;700&family=Montserrat:wght@400&display=swap">
<style>
  :root {
    --board: #e1e1e3;
    --navy-deep: #0a1f5c;
    --navy: #0d2c72;
    --navy-soft: #123a86;
    --accent: #1a7fd0;
    --accent-light: #3aa6ff;
    --white: #ffffff;
    --label: #1d1d1f;
    --photo-a: #0b2a66;
    --photo-b: #2f7fc4;
    --photo-c: #9fd4f5;
  }
  * { margin: 0; padding: 0; box-sizing: border-box; }
  html, body { width: 1200px; height: 600px; overflow: hidden; }
  body { background: var(--board); position: relative; font-family: "Montserrat", sans-serif; }

  .banner {
    position: absolute; left: 67px; top: 66px; width: 1067px; height: 267px;
    background: radial-gradient(ellipse at 30% 30%, var(--navy-soft) 0%, var(--navy) 45%, var(--navy-deep) 100%);
    box-shadow: 2px 3px 6px rgba(0,0,0,.35);
    overflow: hidden;
  }
  .banner-wave {
    position: absolute; left: 0; bottom: 0; width: 100%; height: 80px;
  }
  .brand-name {
    position: absolute; left: 30px; top: 135px; width: 190px; text-align: center;
    font-family: "Poppins", sans-serif; font-weight: 600; font-size: 22px;
    letter-spacing: 1px; color: var(--white);
  }
  .headline {
    position: absolute; left: 248px; top: 56px;
    font-family: "Poppins", sans-serif; color: var(--white);
    font-size: 35px; line-height: 47px; white-space: nowrap;
  }
  .headline strong { font-weight: 700; display: block; letter-spacing: -0.3px; }
  .headline span { font-weight: 400; display: block; }

  .photo {
    position: absolute; right: 0; top: 0; width: 287px; height: 267px;
    background: linear-gradient(120deg, var(--photo-a) 0%, var(--photo-b) 45%, var(--photo-c) 70%, var(--photo-a) 100%);
    clip-path: polygon(0 0, 100% 0, 100% 100%, 7px 100%, 77px 131px);
  }
  .photo-edge { position: absolute; right: 0; top: 0; width: 287px; height: 267px; }

  .caption {
    position: absolute; font-size: 16px; color: var(--label); text-align: center;
  }
  .caption-banner { left: 0; width: 1200px; top: 360px; }

  .square {
    position: absolute; width: 79px; height: 79px; top: 424px;
    display: flex; align-items: center; justify-content: center;
    box-shadow: 1px 2px 4px rgba(0,0,0,.3);
    font-family: "Poppins", sans-serif; font-weight: 600; font-size: 12px; letter-spacing: .5px;
  }
  .square-dark { left: 133px; background: linear-gradient(160deg, var(--navy-soft), var(--navy-deep)); color: var(--white); }
  .square-light { left: 288px; background: var(--white); color: var(--accent); }
  .caption-square { top: 522px; width: 120px; }
  .caption-dark { left: 112px; }
  .caption-light { left: 268px; }
</style>
</head>
<body>
  <section class="banner">
    <svg class="banner-wave" viewBox="0 0 1067 80" preserveAspectRatio="none" aria-hidden="true">
      <path d="M0 60 C200 20 380 70 560 55 S860 10 1067 40 L1067 80 L0 80 Z" fill="#163f8f" opacity=".35"/>
      <path d="M420 80 C560 40 700 60 820 30 L860 80 Z" fill="#1f4fa3" opacity=".3"/>
    </svg>
    <div class="brand-name">QUANTVALE</div>
    <h1 class="headline">
      <strong>Data-Driven Stock market</strong>
      <strong>Portfolio management</strong>
      <span>using quantitative analysis.</span>
    </h1>
    <div class="photo" role="img" aria-label="Photo of an analyst in a suit holding a tablet in front of glowing stock chart graphics"></div>
    <svg class="photo-edge" viewBox="0 0 287 267" aria-hidden="true">
      <polyline points="2,0 78,131 8,267" fill="none" stroke="var(--accent)" stroke-width="5"/>
    </svg>
  </section>
  <p class="caption caption-banner">Mosvane Banner 1600x400 px</p>

  <div class="square square-dark">QUANTVALE</div>
  <div class="square square-light">QUANTVALE</div>
  <p class="caption caption-square caption-dark">120x120 px</p>
  <p class="caption caption-square caption-light">120x120 px</p>
</body>
</html>
```